Financial advisory firm needs new business card design

Business card design , simple , elegant, professional. Will use existing logo. One side should be a solid blue background (matching blue in Logo) . info side should have basic info, maybe two color panes. one white, one a different color..maybe light grey. Please visit our website to get feel for colors and business. www.tallowmeadwealth.com

Industry/Entity Type

Financial Service

Contact Information for Business Card

Basic info..minimalist, modern, approach

Colors

Designer to choose colors to be used in the design.

Requirements
Must have
• Important regulatory requirement. The following disclosure MUST be included somewhere on the business card. It can be either front, or back, and it may be in a smaller font (but has to be legible). My interest is to satisfy the requirement with the least possible disruption to the beauty of the card design.
• All securities offered through the Harrowgate Capital, Inc. Oakhurst Lane, NJ. Member QOLTA/DWEM. Advisory services provided through HC Advisory Services, Inc. an PBR Registered Investment Advisor.

```html
<!DOCTYPE html>
<html lang="en">
<head>
<meta charset="utf-8">
<title>Tallowmead Wealth – Business Card</title>
<link rel="stylesheet" href="https://fonts.googleapis.com/css2?family=Poppins:wght@400;500;700&display=swap">
<style>
  :root {
    --stage: #2b2b2e;
    --brand-blue: #0b4f8c;
    --brand-blue-bright: #2f78c4;
    --spot-navy: #10295a;
    --disclosure-ink: #d6e3f3;
    --ink: #1c1c20;
    --paper: #ffffff;
  }
  * { margin: 0; padding: 0; box-sizing: border-box; }
  html, body { width: 1200px; height: 880px; overflow: hidden; background: var(--stage); }
  body { position: relative; font-family: "Poppins", sans-serif; }

  .card {
    position: absolute;
    left: 250px;
    width: 700px;
    height: 400px;
    overflow: hidden;
    box-shadow: 0 12px 30px rgba(0,0,0,.45);
  }
  .card--back { top: 27px; background: var(--brand-blue); }
  .card--front { top: 453px; background: var(--paper); }

  .wordmark {
    position: absolute;
    display: flex;
    align-items: center;
    gap: 12px;
    font-weight: 700;
    letter-spacing: 2px;
    text-transform: uppercase;
    white-space: nowrap;
  }
  .wordmark__dot { border-radius: 50%; flex: none; }

  .card--back .wordmark {
    left: 0; right: 0; top: 125px;
    justify-content: center;
    font-size: 34px;
    color: var(--spot-navy);
  }
  .card--back .wordmark__dot { width: 24px; height: 24px; background: var(--spot-navy); }

  .disclosure {
    position: absolute;
    left: 70px; right: 70px; top: 262px;
    text-align: center;
    font-size: 12px;
    line-height: 1.5;
    color: var(--disclosure-ink);
  }

  .waves { position: absolute; inset: 0; }

  .card--front .wordmark {
    left: 40px; top: 62px;
    font-size: 24px;
    color: var(--ink);
  }
  .card--front .wordmark__dot { width: 20px; height: 20px; background: var(--brand-blue-bright); }

  .person { position: absolute; left: 60px; top: 168px; }
  .person__name { font-size: 21px; font-weight: 700; color: var(--ink); letter-spacing: .5px; text-transform: uppercase; line-height: 1.3; }
  .person__role { font-size: 13px; font-weight: 500; color: var(--brand-blue-bright); text-transform: uppercase; letter-spacing: .5px; }

  .contact {
    position: absolute;
    right: 26px; top: 232px;
    list-style: none;
    color: var(--paper);
    font-size: 13px;
    text-align: right;
  }
  .contact__item { display: flex; justify-content: flex-end; align-items: center; gap: 10px; line-height: 26px; white-space: nowrap; }
  .contact__icon { width: 13px; height: 13px; flex: none; fill: var(--paper); }
</style>
</head>
<body>

<section class="card card--back" aria-label="Card back">
  <div class="wordmark"><span class="wordmark__dot"></span>Tallowmead Wealth</div>
  <p class="disclosure">
    All securities offered through the Harrowgate Capital, Inc. Oakhurst Lane, NJ.<br>
    Member QOLTA/DWEM. Advisory services provided through HC Advisory Services, Inc.<br>
    an PBR Registered Investment Advisor.
  </p>
</section>

<section class="card card--front" aria-label="Card front">
  <svg class="waves" viewBox="0 0 700 400" width="700" height="400" aria-hidden="true">
    <path d="M700 0 L540 0 C450 20 400 150 300 230 C220 300 120 350 0 370 L0 400 L700 400 Z" fill="var(--brand-blue)"/>
    <path d="M580 14 C480 50 440 190 340 260 C250 320 140 360 30 385 C160 355 270 310 355 250 C450 180 490 60 580 14 Z" fill="var(--paper)"/>
    <path d="M310 200 C280 280 160 310 0 322 L0 336 C180 328 292 295 310 200 Z" fill="var(--ink)"/>
  </svg>

  <div class="wordmark"><span class="wordmark__dot"></span>Tallowmead Wealth</div>

  <div class="person">
    <p class="person__name">Dorian Velsky</p>
    <p class="person__role">President &amp; Founder</p>
  </div>

  <ul class="contact">
    <li class="contact__item">(555) 214-0386
      <svg class="contact__icon" viewBox="0 0 24 24"><path d="M6.6 10.8a15.1 15.1 0 0 0 6.6 6.6l2.2-2.2a1 1 0 0 1 1-.25 11.4 11.4 0 0 0 3.6.57 1 1 0 0 1 1 1V20a1 1 0 0 1-1 1A17 17 0 0 1 3 4a1 1 0 0 1 1-1h3.5a1 1 0 0 1 1 1c0 1.25.2 2.45.57 3.57a1 1 0 0 1-.25 1z"/></svg>
    </li>
    <li class="contact__item">info@tallowmeadwealth.com
      <svg class="contact__icon" viewBox="0 0 24 24"><path d="M2 5h20v14H2z M4 7v.5l8 5 8-5V7z" fill-rule="evenodd"/></svg>
    </li>
    <li class="contact__item">www.tallowmeadwealth.com
      <svg class="contact__icon" viewBox="0 0 24 24"><path d="M12 2a10 10 0 1 0 0 20 10 10 0 0 0 0-20zm0 2a8 8 0 0 1 7.7 6h-3.6a14 14 0 0 0-2-5.7A8 8 0 0 1 12 4zm-2 .3A14 14 0 0 0 7.9 10H4.3A8 8 0 0 1 10 4.3zM4.3 14h3.6a14 14 0 0 0 2 5.7A8 8 0 0 1 4.3 14zm9.8 5.7a14 14 0 0 0 2-5.7h3.6a8 8 0 0 1-5.6 5.7zM10 10a12 12 0 0 1 2-5 12 12 0 0 1 2 5zm0 4h4a12 12 0 0 1-2 5 12 12 0 0 1-2-5z"/></svg>
    </li>
    <li class="contact__item">14 Fenwick Row, Suite 302B, Alderbrook, NJ 07190
      <svg class="contact__icon" viewBox="0 0 24 24"><path d="M12 2a7 7 0 0 0-7 7c0 5.2 7 13 7 13s7-7.8 7-13a7 7 0 0 0-7-7zm0 9.5A2.5 2.5 0 1 1 12 6.5a2.5 2.5 0 0 1 0 5z"/></svg>
    </li>
  </ul>
</section>

</body>
</html>
```